Quillmere Voyage Care Web Page

To create a web page that has the number 1 goal of converting Zorvix Ad / Trellisgram Ads clicks into paying customers.
The site will feed into a web application where travellers can enter their trip and purchase a Voyawell Ready Pack.
The page / site needs to be able to tell people what we do and encourage them to start the process of getting a Voyawell Ready Pack.
It should be a wordpress theme.
Please see the attached brief for more information.

```html
<!DOCTYPE html>
<html lang="en">
<head>
<meta charset="utf-8">
<title>Quillmere Voyage Care</title>
<link href="https://fonts.googleapis.com/css2?family=Catamaran:wght@500;700;800&family=Arimo:wght@400;700&display=swap" rel="stylesheet">
<style>
:root{
  --navy:#1c2d55;
  --navy-deep:#17264a;
  --sky:#5aaad6;
  --sky-soft:#8cc4e4;
  --ink:#2b2b2b;
  --muted:#7a7a7a;
  --footer:#2e2e2e;
  --white:#ffffff;
}
*{box-sizing:border-box;margin:0;padding:0}
html,body{width:1200px;height:4144px;overflow:hidden}
body{position:relative;background:var(--white);font-family:"Arimo",Arial,sans-serif;color:var(--ink)}
.abs{position:absolute}
.heading{font-family:"Catamaran","Trebuchet MS",sans-serif;font-weight:800;letter-spacing:1px}
.line{display:block;white-space:nowrap}
.btn{position:absolute;display:flex;align-items:center;justify-content:center;border-radius:28px;color:var(--white);font-family:"Catamaran",sans-serif;font-weight:700;font-size:15px;letter-spacing:.5px;text-transform:uppercase}
.btn-grad{background:linear-gradient(180deg,#4c8fc2 0%,var(--navy) 100%)}
.btn-sky{background:var(--sky)}
.btn-navy{background:var(--navy)}
.btn-ghost{border:2px solid rgba(255,255,255,.8)}

/* header */
.topbar{left:320px;top:0;width:880px;height:66px;background:var(--navy);clip-path:polygon(0 0,100% 0,100% 100%,30px 100%)}
.contact{top:0;height:66px;display:flex;align-items:center;color:var(--white);font-size:15px}
.contact b{margin:0 12px 0 16px}
.contact .icon{width:44px;height:44px;border-radius:50%;background:var(--sky);display:flex;align-items:center;justify-content:center}
.brand-tab{left:77px;top:0;width:176px;height:209px;background:var(--white);border-radius:0 0 60px 60px;display:flex;flex-direction:column;align-items:center;justify-content:flex-end;padding-bottom:36px;z-index:2}
.brand-tab .dot{width:44px;height:44px;border-radius:50%;background:var(--sky);margin-bottom:14px}
.brand-name{font-family:"Catamaran",sans-serif;font-weight:700;font-size:20px;line-height:1.1;text-align:center;color:var(--navy)}
.nav{top:110px;left:443px;display:flex;gap:66px;font-size:15px;color:#222}

/* hero */
.hero{left:0;top:174px;width:1200px;height:600px;background:linear-gradient(100deg,#c49a5c 0%,#9fa99a 30%,#6fb3cf 55%,#5fb0d8 100%)}
.hero-kicker{left:630px;top:288px;color:var(--white);font-family:"Catamaran",sans-serif;font-weight:500;font-size:36px;letter-spacing:2px}
.hero-title{left:628px;top:352px;color:var(--white);font-size:50px;line-height:66px}

/* pack section */
.sec-title{font-size:38px;color:var(--navy);text-align:center}
.sec-title span{color:var(--sky)}
.dest{top:997px;width:200px;text-align:center}
.dest .pic{width:148px;height:148px;border-radius:50%;margin:0 auto 26px;background:linear-gradient(160deg,#6db7dc,#3e8fb8 55%,#a88c5c)}
.dest p{color:var(--sky);font-weight:700;font-size:17px}

/* about */
.about{left:0;top:1395px;width:600px;height:524px;background:var(--navy)}
.about-photo{left:600px;top:1395px;width:600px;height:524px;background:linear-gradient(120deg,#c9b7a2 0%,#e4d6c2 40%,#7fb6c0 70%,#d9c9b2 100%)}
.about h2{position:absolute;left:100px;top:118px;color:var(--white);font-size:33px;line-height:49px}
.about p{position:absolute;left:100px;top:238px;width:444px;color:var(--white);font-size:14.5px;line-height:24px;text-align:justify}

/* why buy */
.why-img{left:100px;top:2067px;width:481px;height:415px;border-radius:240px 240px 200px 40px;background:linear-gradient(135deg,#9fc8d8 0%,#4f7f97 45%,#d9c36a 75%,#c8ccd0 100%)}
.why h2{position:absolute;left:648px;top:2090px;font-size:32px;line-height:49px;color:var(--navy)}
.why h2 .line + .line{color:var(--sky)}
.ticks{position:absolute;left:648px;top:2210px;width:460px;list-style:none}
.ticks li{position:relative;padding-left:34px;font-size:14.5px;line-height:26px;margin-bottom:16px}
.ticks li svg{position:absolute;left:0;top:5px}

/* band */
.band{left:0;top:2632px;width:1200px;height:465px;background:linear-gradient(100deg,#3d6e9c 0%,#4f86b6 50%,#6da3cc 100%)}
.band h2{position:absolute;top:120px;width:1200px;text-align:center;color:var(--white);font-size:36px;white-space:nowrap}
.band p{position:absolute;left:160px;top:200px;width:880px;text-align:center;color:var(--white);font-size:14.5px;line-height:26px}

/* cards */
.card{top:3211px;width:480px;height:397px;border:4px solid var(--sky);border-radius:16px;text-align:center}
.card.alt{border-color:var(--navy)}
.card h3{margin-top:52px;font-family:"Catamaran",sans-serif;font-weight:700;font-size:22px;letter-spacing:.5px;color:var(--navy);white-space:nowrap}
.card.alt h3{color:var(--sky)}
.card p{margin:28px auto 0;width:430px;font-size:13.5px;line-height:22.5px;color:var(--muted)}

/* footer */
.footer{left:0;top:3721px;width:1200px;height:423px;background:var(--footer)}
.f-brand{left:100px;top:3835px;width:175px;display:flex;flex-direction:column;align-items:center}
.f-brand .dot{width:86px;height:86px;border-radius:50%;background:var(--white);margin-bottom:20px}
.f-brand .brand-name{color:var(--white);font-size:26px}
.f-col{top:3838px}
.f-col h4{font-family:"Catamaran",sans-serif;font-weight:700;font-size:23px;color:var(--sky);margin-bottom:18px}
.f-col a{display:block;color:var(--white);text-decoration:none;font-size:17px;line-height:32px}
.field{height:43px;border:1.5px solid #d8d8d8;border-radius:6px;color:#ddd;font-size:13px;display:flex;align-items:center;padding-left:16px}
.captcha{left:833px;top:4017px;width:85px;height:20px;background:#f5f5f5;border:1px solid #bbb;display:flex;align-items:center;gap:4px;padding-left:4px;font-size:7px;color:#555}
.captcha i{width:8px;height:8px;border:1px solid #888;background:#fff}
.copy{top:4083px;width:1200px;text-align:center;color:var(--white);font-size:14px;left:-50px}
</style>
</head>
<body>

<header>
  <div class="abs topbar"></div>
  <div class="abs contact" style="left:378px">
    <span class="icon"><svg width="20" height="20" viewBox="0 0 24 24" fill="#fff"><path d="M6.6 10.8a15.1 15.1 0 0 0 6.6 6.6l2.2-2.2c.3-.3.7-.4 1-.2 1.1.4 2.3.6 3.6.6.6 0 1 .4 1 1V20c0 .6-.4 1-1 1A17 17 0 0 1 3 4c0-.6.4-1 1-1h3.5c.6 0 1 .4 1 1 0 1.3.2 2.5.6 3.6.1.3 0 .7-.2 1z"/></svg></span>
    <b>PHONE :</b>+1 (555) 014 2290
  </div>
  <div class="abs contact" style="left:663px">
    <span class="icon"><svg width="20" height="20" viewBox="0 0 24 24" fill="#fff"><path d="M3 6l9 6 9-6v12H3z"/><path d="M3 5h18l-9 6z"/></svg></span>
    <b>EMAIL :</b>hello@quillmerevoyage.com
  </div>
  <svg class="abs" style="left:1079px;top:22px" width="22" height="22" viewBox="0 0 24 24" fill="none" stroke="#fff" stroke-width="3"><circle cx="10" cy="10" r="7"/><path d="M15 15l6 6"/></svg>

  <div class="abs brand-tab">
    <span class="dot"></span>
    <div class="brand-name">Quillmere<br>Voyage Care</div>
  </div>

  <nav class="abs nav"><span>HOME</span><span>ABOUT US</span><span>DISEASE</span><span>COUNTRY</span></nav>
  <div class="btn btn-grad" style="left:978px;top:97px;width:124px;height:51px">Log in</div>
</header>

<section>
  <div class="abs hero" role="img" aria-label="Smiling young traveller with a backpack looking at her phone in a sunny waterfront town"></div>
  <div class="abs hero-kicker">WELCOME TO</div>
  <h1 class="abs heading hero-title"><span class="line">QUILLMERE VOYAGE</span><span class="line">CARE</span></h1>
  <div class="btn btn-grad" style="left:632px;top:520px;width:145px;height:53px">Get started</div>
</section>

<section>
  <h2 class="abs heading sec-title" style="left:0;top:898px;width:1200px">VOYAWELL <span>READY PACK</span></h2>
  <div class="abs dest" style="left:74px"><div class="pic" role="img" aria-label="Traveller overlooking a turquoise bay"></div><p>Lorem ipsum dolor</p></div>
  <div class="abs dest" style="left:286px"><div class="pic" role="img" aria-label="Traveller in a sun hat beside a tropical limestone island"></div><p>Lorem ipsum dolor</p></div>
  <div class="abs dest" style="left:500px"><div class="pic" role="img" aria-label="Mountain lake reflecting an autumn forest"></div><p>Lorem ipsum dolor</p></div>
  <div class="abs dest" style="left:714px"><div class="pic" role="img" aria-label="Limestone rock rising from a green sea with a longtail boat"></div><p>Lorem ipsum dolor</p></div>
  <div class="abs dest" style="left:926px"><div class="pic" role="img" aria-label="Historic European city square at dusk"></div><p>Lorem ipsum dolor</p></div>
  <div class="btn btn-grad" style="left:531px;top:1229px;width:138px;height:53px">View all</div>
</section>

<section class="abs about">
  <h2 class="heading"><span class="line">WHAT IS QUILLMERE</span><span class="line">VOYAGE CARE?</span></h2>
  <p>Lorem ipsum dolor sit amet, consectetur adipiscing elit, sed do eiusmod tempor incididunt ut labore et dolore magna aliqua. Ut enim ad minim veniam, quis nostrud exercitation ullamco laboris nisi ut aliquip ex ea commodo consequat. Duis aute irure dolor in reprehenderit in voluptate velit esse cillum dolore eu fugiat nulla pariatur.</p>
  <div class="btn btn-sky" style="left:100px;top:410px;width:136px;height:53px">Learn more</div>
</section>
<div class="abs about-photo" role="img" aria-label="Two friends laughing while reading a paper map in front of an ornate old building"></div>

<section class="why">
  <div class="abs why-img" role="img" aria-label="Suitcases standing by an airport window"></div>
  <h2 class="heading"><span class="line">WHY BUY A VOYAWELL</span><span class="line">READY PACK</span></h2>
  <ul class="ticks">
    <li><svg width="18" height="18" viewBox="0 0 18 18"><circle cx="9" cy="9" r="9" fill="#1c2d55"/><path d="M7 5l4 4-4 4" stroke="#fff" stroke-width="2" fill="none"/></svg>Lorem ipsum dolor sit amet, consectetur adipiscing elit, sed do eiusmod tempor</li>
    <li><svg width="18" height="18" viewBox="0 0 18 18"><circle cx="9" cy="9" r="9" fill="#1c2d55"/><path d="M7 5l4 4-4 4" stroke="#fff" stroke-width="2" fill="none"/></svg>Lorem ipsum dolor sit amet, consectetur adipiscing elit, sed do eiusmod tempor</li>
    <li><svg width="18" height="18" viewBox="0 0 18 18"><circle cx="9" cy="9" r="9" fill="#1c2d55"/><path d="M7 5l4 4-4 4" stroke="#fff" stroke-width="2" fill="none"/></svg>Lorem ipsum dolor sit amet, consectetur adipiscing elit, sed do</li>
    <li><svg width="18" height="18" viewBox="0 0 18 18"><circle cx="9" cy="9" r="9" fill="#1c2d55"/><path d="M7 5l4 4-4 4" stroke="#fff" stroke-width="2" fill="none"/></svg>Lorem ipsum dolor sit amet, consectetur adipiscing elit, sed do eiusmod tempor</li>
  </ul>
  <div class="btn btn-grad" style="left:648px;top:2466px;width:114px;height:53px">Buy</div>
</section>

<section class="abs band" role="img" aria-label="Boarding passes, passport and a toy plane on a world map, tinted blue">
  <h2 class="heading">WHAT IS IN A VOYAWELL READY PACK</h2>
  <p>Lorem ipsum dolor sit amet, consectetur adipiscing elit, sed do eiusmod tempor incididunt ut labore et dolore magna aliqua. Ut enim ad minim veniam, quis nostrud exercitation ullamco laboris nisi ut aliquip ex ea commodo consequat. Duis aute irure dolor in reprehenderit in voluptate velit esse cillum dolore eu fugiat nulla pariatur.Sed ut perspiciatis unde omnis iste natus error sit voluptatem accusantium doloremque laudantium, totam rem aperiam, eaque ipsa quae ab illo inventore veritatis et quasi architecto beatae vitae dicta sunt explicabo.</p>
  <div class="btn btn-ghost" style="left:528px;top:355px;width:144px;height:52px">Learn more</div>
</section>

<section>
  <article class="abs card" style="left:98px">
    <h3>WHAT VACCINES DO I NEED FOR....</h3>
    <p>Sed ut perspiciatis unde omnis iste natus error sit voluptatem accusantium doloremque laudantium, totam rem aperiam, eaque ipsa quae ab illo inventore veritatis et quasi architecto beatae vitae dicta sunt explicabo. Nemo enim ipsam voluptatem quia voluptas sit aspernatur aut odit aut fugit, sed quia consequuntur magni dolores eos qui ratione voluptatem sequi nesciunt.</p>
    <div class="btn btn-navy" style="left:164px;top:287px;width:145px;height:52px">Learn more</div>
  </article>
  <article class="abs card alt" style="left:621px">
    <h3>WHAT ANTIMALARIALS DO I NEED FOR...</h3>
    <p>Sed ut perspiciatis unde omnis iste natus error sit voluptatem accusantium doloremque laudantium, totam rem aperiam, eaque ipsa quae ab illo inventore veritatis et quasi architecto beatae vitae dicta sunt explicabo. Nemo enim ipsam voluptatem quia voluptas sit aspernatur aut odit aut fugit, sed quia consequuntur magni dolores eos qui ratione voluptatem sequi nesciunt.</p>
    <div class="btn btn-sky" style="left:164px;top:287px;width:145px;height:52px">Learn more</div>
  </article>
</section>

<footer>
  <div class="abs footer"></div>
  <div class="abs f-brand"><span class="dot"></span><div class="brand-name">Quillmere<br>Voyage Care</div></div>
  <div class="abs f-col" style="left:378px"><h4>QUICK LINKS</h4><a>Home</a><a>About Us</a><a>Disease</a><a>Country</a></div>
  <div class="abs f-col" style="left:608px"><h4>OTHER LINKS</h4><a>Privacy</a><a>Terms</a><a>Refund</a><a>Disclaimer</a></div>
  <div class="abs f-col" style="left:833px"><h4>CONTACT US</h4></div>
  <div class="abs field" style="left:833px;top:3901px;width:131px">Name</div>
  <div class="abs field" style="left:972px;top:3901px;width:130px">Name</div>
  <div class="abs field" style="left:833px;top:3960px;width:269px">Message</div>
  <div class="abs captcha"><i></i>Not a robot</div>
  <div class="btn btn-sky" style="left:1009px;top:4017px;width:93px;height:40px;font-size:12px">Send</div>
  <div class="abs copy">©Copyrights 2023 Quillmere Voyage Care &nbsp;| &nbsp; All Rights Reserved</div>
</footer>

</body>
</html>
```